Website for the recruitment firm velmo

Objective :

Create a modern, elegant, and understated website with a touch of sophistication. The site must be fully custom-coded (or custom-coded on WordPress), responsive, and fast, reflecting the quality and high standards of our firm.

It must be bilingual (FR/EN), with a language selector visible in the header.

About velmo.

velmo. is a high-end recruitment firm, led by experienced consultants—employees and freelancers—and supported by a dedicated team of recruitment managers. Our hybrid approach allows us to handle complex, confidential, or high-volume projects with rigor and agility.

We operate across several business verticals:

Executive

Finance & Advisory (accounting, management control, treasury, corporate finance, financial consulting or investment banking)

Legal

Audit & Expertise

People & Office

Supply & Purchasing

Industry & Engineering

Our approach is based on a balance between human know-how and cutting-edge technologies (AI, automation, data) to respond to recruitment challenges with accuracy, responsiveness and impact.

Slogan: Expertise at the service of every recruitment.

Purpose of the site:

Client side: present our expertise, our values, our support.

Candidate side: allow the search for offers, by expertise.

On the consultant side: encouraging freelancers or employees to join us.

Structure & pages requested:

Welcome

Main banner with slogan and strong visual (possibility of a background video like maisontalvo.example — for a modern and dynamic look)

Clear redirection to both paths: “I’m looking for talent” / “I want to join velmo. ”

Quick presentation of expertise with redirection to each dedicated page

Highlighting values

About

Our mission

Our values (excellence, flexibility, partnership)

Our hybrid operation (in-house and independent consultants)

The recruitment team and the support offered

Expertise (1 page per vertical, with color code specific to each division)

Description of the professions recruited

Key skills

Typical customer profiles

Testimonials or case studies (placeholder)

Button/CTA to offers corresponding to this expertise

Job offers

Page with filter by expertise

“Join velmo” option with our internal offers (consultants, recruitment managers, etc.)

Join us

Why work with velmo.

Independent vs. employee path

Tools provided, support, internal training

Highlighting the support team and recruitment managers

Contact

Form

Email + LinkedIn link

Design requirements:

Font: Gazette LT Std or contemporary serif with a strong identity

Color code by division (the background or page elements must match the color of the expertise):

velmo. / velmo.group. → #000000 (black)

velmo.executive. → #2F4F4F (dark green)

velmo.finance&advisory. → #0B1E36 (midnight blue)

velmo.people&office. → #f2b8b8 (powder pink)

velmo.audit&expertise. → #993294 (plum)

velmo.legal. → #d9a00f (yellow gold)

velmo.supply&purchasing. → #CE8946 (rust bronze)

velmo.industry&engineering. → #9e9b9e (light silver gray)

Technical features:

100% responsive and mobile-friendly design

Fast charging

Own structure (SEO-friendly)

Simple back-office interface for updating offers

Language selector FR / EN

Inspirations to consult:

For the tree structure, tabs and ergonomics: bristow-lane.example

For visual ambiance / video / animation: maisontalvo.example

Expected deliverables:

Full site (online or compressed file)

All source files (HTML/CSS/JS or custom Wordpress)

Favicon

Brand guideline (PDF) with:

Typographies used

HEX color codes

Margins and line spacing

Examples of use of light and dark background logo

Optional: template for email signature

Objective
Design a modern, elegant and clean website with a touch of sophistication. The site must be fully custom-coded (or built with custom WordPress development), responsive, fast, and reflect the premium standards and quality of our recruitment firm.

It must be bilingual (FR/EN), with a clearly visible language selector in the header.

About velmo.
velmo. is a premium recruitment firm driven by experienced consultants — whether in-house or freelance — supported by a dedicated team of recruitment coordinators. Our hybrid model allows us to handle complex, confidential, or high-volume recruitment assignments with both precision and agility.

We operate across several verticals:

Executive

Finance & Advisory (accounting, controlling, treasury, corporate finance, investment banking advisory)

Legal

Audit & Expertise

People & Office

Supply & Purchasing

Industry & Engineering

Our approach combines human expertise with cutting-edge technologies (AI, automation, data) to tackle recruitment challenges with accuracy, speed, and impact.

Tagline: Expertise serving every recruitment need.

Website Purpose
Client-facing: highlight our expertise, values, and recruitment support model.

Candidate-facing: allow job seekers to explore openings by area of expertise.

Consultant-facing: attract freelance or in-house recruiters to join velmo.

Site Structure & Required Pages
Home
Hero banner with tagline and impactful visual (option for background video, eg maisontalvo. That)

Clear user path: “I'm looking to hire” / “I want to join velmo. ”

Quick intro to our expertise areas with links to each division page

Highlight our values and unique model

About Us
Our mission

Our hybrid recruitment model (internal consultants + freelancers)

Our recruitment support team and how we work

Expertise (1 page per vertical, using the division's brand color)
Each division page should include:

Description of roles we recruit

Key skills

Typical client profiles

Placeholder for testimonials or success stories

CTA linking to job openings relevant to the division

Verticals:

Executive

Finance & Advisory

Legal

Audit & Expertise

People & Office

Supply & Purchasing

Industry & Engineering

Job Offers
Central job board with filter by expertise

Section: “Join velmo. ” with internal positions (consultants, recruitment coordinators, etc.)

Join Us
Why join velmo.

Independent vs. permanent contract path

Tools, training and operational support

Highlight the internal sourcing and recruitment support team

Contact
Contact form

Email + LinkedIn link

Design Requirements
Font: Gazette LT Std or similar contemporary serif with strong identity

Each vertical should have its own dedicated brand color applied to its page background or key elements:

Division HEX Code Color Description
velmo. /velmo.group. #000000 Black
velmo.executive #2F4F4F Dark green
velmo.finance&advisory #0B1E36 Navy blue
velmo.people&office #f2b8b8 Powder pink
velmo.audit&expertise #993294 Plum
velmo.legal #d9a00f Golden yellow
velmo.supply&purchasing #CE8946 Rust bronze
velmo. industry&engineering #9e9b9e Light silver gray

Technical Features
Fully responsive and mobile-friendly

Fast loading

Clean structure, SEO optimized

Simple back-office interface for job posting and updates

Bilingual switch: FR / EN

Inspirations
For navigation, structure, and user interface:
🔗 https://www.bristow-lane.example/fr/fr/

For visual style, animations, and dynamic video intro:
🔗 https://maisontalvo.example/

Deliverables
Fully functional website (live or delivered as a complete package)

All source files (HTML/CSS/JS or custom WordPress)

Favicon

Brand guideline (PDF) including:

Fonts used

HEX color codes

Spacing and layout guidelines

Logo usage on dark/light backgrounds

Optional: email signature template

Hi, A few clarifications to guide the website structure. The site should be clearly built around three main sections, each addressing a specific target audience: 1. For Clients – “Looking to hire?” This section will highlight our recruitment services, industry expertise, and tailored approach. 2. For Candidates – “Looking for a job?” A space where candidates can explore job offers by sector and apply directly. 3. For Experts – “Want to join us?” This area is for recruitment professionals (consultants or talent acquisition specialists) interested in joining velmo., either as employees or as independents. It should showcase the tools, support, and working environment we offer. These three user paths should be clearly visible on the homepage, using clear buttons or dedicated sections to ensure smooth navigation.

• Gazette LT Std

• Essentials – Section Ideas Our hybrid model → Clear presentation of employee/freelance cohabitation, and how it brings flexibility and efficiency to clients. Our quality commitment → Rigorous methodology, transparency, customer satisfaction, tailor-made support. Our augmented approach → Highlighting the use of AI tools, intelligent CRM, automated multi-channel sourcing, predictive tests, etc. Our support team → Promotion of the team of recruitment managers who support the consultants, guaranteeing responsiveness and depth in the hunt. Our areas of expertise → Mini-grid or mosaic that links to the main verticals (useful for cross-functional reinforcement).
• CRM / ATS Integration Direct connection with our application management tool (Dorveta type or other), for seamless synchronization of offers, applications and follow-ups. 📱 Progressive web app version (PWA) A site accessible in mobile application mode, for a smooth, fast and accessible offline user experience.

```html
<!DOCTYPE html>
<html lang="en">
<head>
<meta charset="utf-8">
<title>velmo. — Expertise serving every recruitment need</title>
<link rel="stylesheet" href="https://fonts.googleapis.com/css2?family=Noto+Serif:wght@400;600;700;800&display=swap">
<style>
:root{
  --black:#000000;
  --ink:#2b2b2b;
  --text:#3a3a3a;
  --muted:#555555;
  --executive:#2F4F4F;
  --finance:#0B1E36;
  --legal:#d9a00f;
  --audit:#993294;
  --bronze:#CE8946;
  --accent:#d3812f;
  --light:#f3f3f3;
  --footer:#262626;
  --white:#ffffff;
}
*{box-sizing:border-box;margin:0;padding:0}
html,body{width:1200px;height:2922px;overflow:hidden}
body{font-family:"Noto Serif",Georgia,serif;color:var(--text);background:var(--white);position:relative}
a{color:inherit;text-decoration:none}

/* header */
.site-header{position:absolute;top:0;left:0;width:1200px;height:82px;background:var(--white)}
.brand{position:absolute;left:75px;top:12px;font-size:42px;font-weight:800;color:var(--black);letter-spacing:-1px}
.main-nav{position:absolute;left:492px;top:35px;display:flex;gap:40px;font-size:15px;color:var(--ink)}
.main-nav .active{color:var(--accent);font-weight:600}
.lang{position:absolute;left:1056px;top:28px;width:71px;height:31px;border:1px solid #bbb;border-radius:3px;font-size:11px;display:flex;align-items:center;justify-content:center;gap:5px;color:#333}

/* hero */
.hero{position:absolute;top:82px;left:0;width:1200px;height:570px;background:linear-gradient(100deg,#6b6a66 0%,#8a8580 30%,#a49b93 55%,#3e3c3e 85%,#2a2a2f 100%)}
.hero-title{position:absolute;top:180px;left:0;width:1200px;text-align:center;color:var(--white);font-size:62px;line-height:62px;font-weight:700;letter-spacing:1px}
.hero-actions{position:absolute;top:330px;left:342px;display:flex;gap:29px}
.btn{display:inline-flex;align-items:center;justify-content:center;height:60px;width:245px;color:var(--white);font-size:20px;font-weight:600}
.btn-hire{background:var(--legal)}
.btn-join{background:var(--bronze)}
.play{position:absolute;left:996px;top:484px;width:204px;height:45px;border-radius:23px 0 0 23px;background:rgba(150,150,150,.8);display:flex;align-items:center;gap:10px;padding-left:4px;color:var(--white);font-size:15px;font-weight:600;text-decoration:underline}

/* about */
.about-label{position:absolute;left:75px;top:720px;font-size:42px;font-weight:700;color:var(--ink)}
.logo-large{position:absolute;left:72px;width:350px;font-size:84px;font-weight:800;color:var(--black);letter-spacing:-2px;line-height:1;white-space:nowrap}
.divider{position:absolute;left:432px;width:2px;background:var(--black)}
.about-text{position:absolute;left:464px;top:748px;width:660px;font-size:19.5px;line-height:30.5px;color:var(--text)}

/* expertise */
.expertise{position:absolute;top:1010px;left:0;width:1200px;height:595px;background:var(--light)}
.section-title{position:absolute;top:68px;left:0;width:1200px;text-align:center;font-size:43px;font-weight:700;color:var(--ink)}
.card{position:absolute;top:160px;width:241px;height:325px;border-radius:6px;color:var(--white);padding:0 18px}
.card h3{position:absolute;left:18px;bottom:20px;font-size:25px;line-height:27px;font-weight:700}
.card .icon{position:absolute;left:18px;width:104px;height:104px;border:2px solid rgba(255,255,255,.85);border-radius:8px}
.card-exec{left:75px;background:linear-gradient(160deg,#3c5b57,#22403c)}
.card-exec h3{top:150px;bottom:auto}
.card-exec p{position:absolute;left:18px;top:186px;width:205px;font-size:15.5px;line-height:22.5px}
.card-exec .more{position:absolute;left:18px;top:268px;font-size:16px;color:var(--legal)}
.card-fin{left:344px;background:var(--finance)}
.card-legal{left:615px;background:var(--legal)}
.card-audit{left:884px;background:var(--audit)}
.slider-arrows{position:absolute;left:1140px;top:300px}

/* values */
.values-label{position:absolute;left:75px;top:1668px;font-size:40px;font-weight:700;color:var(--ink)}
.value{position:absolute;top:1685px;width:200px;text-align:center}
.value .vicon{width:62px;height:62px;margin:0 auto;border-radius:50%;background:#efd9ee}
.value h4{margin-top:30px;font-size:25px;font-weight:600;color:#5a5a5a;letter-spacing:.5px}
.value p{margin-top:8px;font-size:15.5px;line-height:22.5px;color:#555}

/* hybrid */
.hybrid-media{position:absolute;left:0;top:1948px;width:675px;height:490px;border-radius:0 8px 8px 0;background:linear-gradient(135deg,#2d3f5c 0%,#1d2e4a 45%,#0f1a2c 100%)}
.hybrid-card{position:absolute;left:587px;top:2013px;width:613px;height:359px;background:var(--white);border-radius:8px 0 0 8px;padding:40px 28px}
.hybrid-card h2{font-size:41px;line-height:44px;font-weight:700;color:var(--ink)}
.hybrid-card p{margin-top:22px;width:520px;font-size:19px;line-height:30.5px;color:var(--text)}
.btn-learn{margin-top:26px;width:164px;height:55px;background:var(--audit);font-size:18px}

/* footer */
.site-footer{position:absolute;top:2512px;left:0;width:1200px;height:410px;background:var(--footer);color:var(--white);overflow:hidden}
.footer-deco{position:absolute;left:540px;top:150px;font-size:300px;font-weight:800;color:#2d2d2d;letter-spacing:-10px;line-height:1}
.footer-brand{position:absolute;left:75px;top:55px;font-size:56px;font-weight:800;color:#b5b5b5;letter-spacing:-2px}
.copy{position:absolute;left:76px;top:162px;font-size:13px;line-height:23px}
.social{position:absolute;left:76px;top:237px;display:flex;gap:18px}
.social span{width:22px;height:22px;border:1.5px solid var(--white);border-radius:3px}
.social span.on{border-color:var(--accent)}
.fcol{position:absolute;top:55px}
.fcol h5{font-size:21px;font-weight:600;margin-bottom:18px}
.fcol li{list-style:none;font-size:13.5px;height:36px}
.fcol .addr{font-size:13.5px;line-height:26px}
</style>
</head>
<body>

<header class="site-header">
  <a class="brand" href="#">velmo.</a>
  <nav class="main-nav">
    <a class="active" href="#">Home</a>
    <a href="#">About Us</a>
    <a href="#">Expertise</a>
    <a href="#">Jobs</a>
    <a href="#">Contact Us</a>
    <a href="#">Join Us</a>
  </nav>
  <div class="lang">
    <svg width="11" height="11" viewBox="0 0 12 12"><circle cx="6" cy="6" r="5" fill="none" stroke="#333"/><path d="M1 6h10M6 1c-2.5 3-2.5 7 0 10M6 1c2.5 3 2.5 7 0 10" fill="none" stroke="#333"/></svg>
    EN
    <svg width="9" height="6" viewBox="0 0 9 6"><path d="M1 1l3.5 3.5L8 1" fill="none" stroke="#333" stroke-width="1.5"/></svg>
  </div>
</header>

<section class="hero" role="img" aria-label="Photo of a recruitment interview between three professionals in a bright office">
  <h1 class="hero-title">Expertise serving every<br>recruitment need</h1>
  <div class="hero-actions">
    <a class="btn btn-hire" href="#">I'm looking to hire</a>
    <a class="btn btn-join" href="#">I want to join velmo.</a>
  </div>
  <a class="play" href="#">
    <svg width="38" height="38" viewBox="0 0 38 38"><circle cx="19" cy="19" r="16" fill="none" stroke="#e0a814" stroke-width="3"/><path d="M15 11l12 8-12 8z" fill="#e0a814"/></svg>
    Play video
  </a>
</section>

<div class="about-label">About</div>
<div class="logo-large" style="top:800px">velmo.</div>
<div class="divider" style="top:730px;height:195px"></div>
<p class="about-text">velmo. is a premium recruitment firm driven by experienced consultants — whether in-house or freelance — supported by a dedicated team of recruitment coordinators. Our hybrid model allows us to handle complex, confidential, or high-volume recruitment assignments with both precision and agility.</p>

<section class="expertise">
  <h2 class="section-title">Our Expertise Areas</h2>
  <article class="card card-exec" role="img" aria-label="Executive division card with portrait photo background">
    <div class="icon" style="top:50px;width:66px;height:66px"></div>
    <h3>Executive</h3>
    <p>Duis aute irure dolor in reprehenderit in voluptate velit esse cillum.</p>
    <a class="more" href="#">Read More</a>
  </article>
  <article class="card card-fin">
    <div class="icon" style="top:118px"></div>
    <h3>Finance &amp;<br>Advisory</h3>
  </article>
  <article class="card card-legal">
    <div class="icon" style="top:118px"></div>
    <h3>Legal</h3>
  </article>
  <article class="card card-audit">
    <div class="icon" style="top:118px"></div>
    <h3>Audit &amp;<br>Expertise</h3>
  </article>
  <svg class="slider-arrows" width="30" height="58" viewBox="0 0 30 58"><path d="M4 14h16M14 6l8 8-8 8" fill="none" stroke="#222" stroke-width="4"/><path d="M26 46H10M16 38l-8 8 8 8" fill="none" stroke="#999" stroke-width="4"/></svg>
</section>

<div class="values-label">Our Values at</div>
<div class="logo-large" style="top:1745px">velmo.</div>
<div class="divider" style="top:1675px;height:195px"></div>
<div class="value" style="left:475px">
  <div class="vicon" role="img" aria-label="Award ribbon icon"></div>
  <h4>Excellence</h4>
  <p>Duis aute irure dolor in reprehenderit in voluptate velit esse cillum</p>
</div>
<div class="value" style="left:696px">
  <div class="vicon" role="img" aria-label="Hand with branching arrows icon"></div>
  <h4>Flexibility</h4>
  <p>Duis aute irure dolor in reprehenderit in voluptate velit esse cillum</p>
</div>
<div class="value" style="left:916px">
  <div class="vicon" role="img" aria-label="Handshake icon"></div>
  <h4>Partnership</h4>
  <p>Duis aute irure dolor in reprehenderit in voluptate velit esse cillum</p>
</div>

<div class="hybrid-media" role="img" aria-label="Photo of a hand selecting candidate profiles on a digital screen with checkmarks"></div>
<section class="hybrid-card">
  <h2>Our Hybrid<br>Recruitment Model</h2>
  <p>A clear and compelling look at our unique blend of employees and freelancers, combining flexibility with efficiency to deliver optimal value for our clients.</p>
  <a class="btn btn-learn" href="#">Learn More</a>
</section>

<footer class="site-footer">
  <div class="footer-deco" aria-hidden="true">velmo.</div>
  <div class="footer-brand">velmo.</div>
  <p class="copy">Copyright © 2025 Company Name<br>All Rights Reserved</p>
  <div class="social" aria-label="Social links">
    <span></span><span class="on"></span><span></span><span></span>
  </div>
  <div class="fcol" style="left:342px">
    <h5>Quick Links</h5>
    <ul><li>Home</li><li>About Us</li><li>Expertise</li><li>Jobs</li><li>Contact Us</li><li>Join Us</li></ul>
  </div>
  <div class="fcol" style="left:615px">
    <h5>Expertise Areas</h5>
    <ul><li>Executive</li><li>Finance &amp; Advisory</li><li>Legal</li><li>Audit &amp; Expertise</li><li>People &amp; Office</li><li>Supply &amp; Purchasing</li><li>Industry &amp; Engineering</li></ul>
  </div>
  <div class="fcol" style="left:884px">
    <h5>Contact Info</h5>
    <p class="addr">48 Orchard Lane Suite 12,<br>Brookhaven 20417, United States</p>
    <p class="addr" style="margin-top:9px">+1 555-014-2290</p>
    <p class="addr" style="margin-top:9px">hello@velmo.example</p>
  </div>
</footer>

</body>
</html>
```